Banner images for web site

Four banner images for Home page of BrightLedgerSystems.com:

Max Width: 575px
Min Width: 550px

Min Height: 300px
Max Height: 250px

Image 1: Use picture of someone swiping a Credit/debit card
Main Text: INNOVATIVE, EFFICIENT AND COST EFFECTIVE CARD PROCESSING SOLUTIONS.
Caption/Call to action text/button: GET STARTED NOW

Image 2: (Use attached picture)
Main Text: ATM PROCESSING, ATM TRANSACTION REPORTING AND ATM ONLINE ACCESS.

Image3: (Use attached picture)
Main Text: WE LISTEN, WE CARE AND WE ARE HERE FOR YOU 24/7.
Caption/Call to action text/button: GET HELP NOW

Image4: (Use picture of middle age, mix race(Black, white, etc) and gender) dressed in business casual or formal business
Main Text: BUILD YOUR CAREER, LIVE YOUR DREAM.
Caption/Call to action text/button: JOIN OUR TEAM

Note: be mindful of our company colors (Green and brown as can be seen at our website)

The idea is to create a sliding banner like the following:
http://www.quorvantpay.us/

The Text in bold on the left, and an illustrative image on the right with slightly fading effect
Updates

Project Deadline Extended
Reason: Other parts of this project have been pushed back so I am extending this deadline by 3 days.

A reminder that this project is simply about images for a slider on the website. I have provided most of the background images to use for that.

We just need it to be expressive, clean and Bold. Use modern, not boring fonts.

Thanks

Project Deadline Extended
Reason: No good design received. Only two designers so far. We need more designs

Target Market(s)

Small merchants, store owners, groceries, restaurants, etc

Industry/Entity Type

Business

Requirements
Must have
• Just banners like the onbes used on this site;
http://www.quorvantpay.us/

```html
<!DOCTYPE html>
<html lang="en">
<head>
<meta charset="utf-8">
<title>BrightLedgerSystems.com – Home Slider Banners</title>
<link rel="stylesheet" href="https://fonts.googleapis.com/css2?family=Arimo:wght@400;700&family=Roboto+Condensed:wght@700&display=swap">
<style>
  :root {
    --page: #ffffff;
    --title-green: #4c6a2c;
    --title-outline: #1f2f10;
    --arrow-green: #7d9a57;
    --arrow-edge: #55703a;
    --btn-green-top: #8aa56a;
    --btn-green-bottom: #4f6b34;
    --atm-panel: rgba(46, 128, 92, 0.82);
    --atm-btn-top: #2f8a62;
    --atm-btn-bottom: #146241;
    --brown-panel: rgba(120, 104, 62, 0.85);
    --gold-top: #c9b56e;
    --gold-bottom: #8a7433;
    --white: #ffffff;
    --ink: #1d1d1d;
  }
  * { box-sizing: border-box; margin: 0; padding: 0; }
  html, body { width: 1200px; height: 1200px; overflow: hidden; background: var(--page); }
  .canvas { position: relative; width: 1200px; height: 1200px; }

  .banner { position: absolute; width: 690px; height: 360px; overflow: hidden; }
  .banner--card { left: 25px; top: 24px; background: linear-gradient(180deg, #eef2f4, #f7f8f9); }
  .banner--atm { left: 486px; top: 418px; }
  .banner--support { left: 25px; top: 816px; }

  .photo { position: absolute; }
  .banner--card .photo {
    left: 200px; top: 110px; width: 490px; height: 250px;
    background: radial-gradient(ellipse at 55% 60%, #3a3c40 0%, #5b5e63 40%, #d9dde0 75%, rgba(238,242,244,0) 100%);
  }
  .banner--atm .photo {
    inset: 0;
    background: linear-gradient(90deg, #5e6663 0%, #8f9894 35%, #b9bdb9 60%, #7a6f68 80%, #a09a95 100%);
  }
  .banner--support .photo {
    inset: 0;
    background: linear-gradient(90deg, #d8dde2 0%, #c9cfd4 35%, #8d7f78 55%, #d7e3ee 75%, #eaf0f5 100%);
  }

  .card-title {
    position: absolute; left: 11px; top: 8px;
    font-family: "Roboto Condensed", sans-serif; font-weight: 700;
    font-size: 35px; line-height: 48px; color: var(--title-green);
    -webkit-text-stroke: 0.8px var(--title-outline);
    text-shadow: 2px 2px 2px rgba(0,0,0,0.25);
  }
  .arrow { position: absolute; }
  .banner--card .arrow { left: 65px; top: 106px; width: 88px; height: 138px; }
  .banner--atm .arrow { left: 67px; top: 200px; width: 38px; height: 54px; }

  .cta {
    position: absolute; display: flex; flex-direction: column; align-items: center; justify-content: center;
    color: var(--white); text-align: center; border-radius: 5px;
    box-shadow: 3px 3px 5px rgba(0,0,0,0.45);
    text-shadow: 1px 1px 2px rgba(0,0,0,0.6);
  }
  .cta small { font-size: 21px; line-height: 24px; }
  .cta strong { font-size: 27px; line-height: 30px; }
  .banner--card .cta {
    left: 23px; top: 252px; width: 168px; height: 76px;
    font-family: "Arimo", sans-serif; font-weight: 700;
    background: linear-gradient(180deg, var(--btn-green-top), var(--btn-green-bottom));
    border: 2px solid #3e5527;
  }
  .banner--atm .cta {
    left: 7px; top: 264px; width: 167px; height: 76px;
    font-family: "Arimo", sans-serif; font-weight: 700;
    background: linear-gradient(180deg, var(--atm-btn-top), var(--atm-btn-bottom));
    border: 2px solid #0e4a30;
  }
  .banner--support .cta {
    left: 46px; top: 266px; width: 203px; height: 55px;
    font-family: "Roboto Condensed", sans-serif; font-size: 27px;
    background: linear-gradient(180deg, var(--gold-top), var(--gold-bottom));
    border: 2px solid #6a5826;
  }

  .atm-panel {
    position: absolute; left: 0; width: 182px; height: 62px;
    background: var(--atm-panel); border-radius: 0 4px 4px 0;
    box-shadow: 2px 2px 4px rgba(0,0,0,0.35);
    font-family: "Arimo", sans-serif; color: var(--white); text-align: center;
    display: flex; flex-direction: column; justify-content: center;
    font-size: 19px; line-height: 28px;
    text-shadow: 1px 1px 2px rgba(0,0,0,0.5);
  }
  .atm-panel--1 { top: 6px; }
  .atm-panel--1 .big { font-size: 24px; }
  .atm-panel--2 { top: 70px; }
  .atm-panel--3 { top: 135px; }

  .care-panel {
    position: absolute; left: 0; width: 322px;
    background: var(--brown-panel); border-radius: 0 6px 6px 0;
    box-shadow: 3px 3px 5px rgba(0,0,0,0.35);
    font-family: "Arimo", sans-serif; color: var(--white);
    text-shadow: 1px 1px 2px rgba(0,0,0,0.45);
  }
  .care-panel--1, .care-panel--2 { height: 60px; font-size: 50px; line-height: 60px; padding-left: 38px; }
  .care-panel--1 { top: 24px; }
  .care-panel--2 { top: 88px; }
  .care-panel--3 { top: 152px; height: 94px; font-size: 27px; line-height: 38px; text-align: center; padding-top: 8px; }
</style>
</head>
<body>
<main class="canvas">

  <section class="banner banner--card" aria-label="Card processing banner">
    <div class="photo" role="img" aria-label="Hand swiping a card through a countertop payment terminal"></div>
    <h2 class="card-title">INNOVATIVE, EFFICIENT AND COST EFFECTIVE<br>CARD PROCESSING SOLUTIONS</h2>
    <svg class="arrow" viewBox="0 0 88 138" aria-hidden="true">
      <polygon points="30,0 58,0 58,80 88,80 44,138 0,80 30,80" fill="var(--arrow-green)" stroke="var(--arrow-edge)" stroke-width="2"/>
    </svg>
    <a class="cta"><small>GET STARTED</small><strong>NOW</strong></a>
  </section>

  <section class="banner banner--atm" aria-label="ATM services banner">
    <div class="photo" role="img" aria-label="Smiling woman inserting a card into an ATM"></div>
    <div class="atm-panel atm-panel--1"><span class="big">ATM</span><span>PROCESSING</span></div>
    <div class="atm-panel atm-panel--2"><span>ATM TRANSACTION</span><span>REPORTING</span></div>
    <div class="atm-panel atm-panel--3"><span>AND ATM</span><span>ONLINE ACCESS</span></div>
    <svg class="arrow" viewBox="0 0 38 54" aria-hidden="true">
      <polygon points="13,0 25,0 25,32 38,32 19,54 0,32 13,32" fill="#2f8a62" stroke="#16603f" stroke-width="1.5"/>
    </svg>
    <a class="cta"><small>GET STARTED</small><strong>NOW</strong></a>
  </section>

  <section class="banner banner--support" aria-label="Customer support banner">
    <div class="photo" role="img" aria-label="Smiling support agent wearing a headset in a call centre"></div>
    <div class="care-panel care-panel--1">We listen</div>
    <div class="care-panel care-panel--2">We care</div>
    <div class="care-panel care-panel--3">And we are here<br>for you 24/7</div>
    <a class="cta">GET HELP NOW</a>
  </section>

</main>
</body>
</html>
```